Lumaro Specs Needs Infographic Designs (Howto: Choose Your Lenses)

We need an infographic to explain to out customers on choosing their lenses. the file attached is the description and steps.

Would need your help to design an infograph which shows clearly the process and make the process looks easy.

You may use icons or graphics to better represent these information.

Colour scheme is orange, dark grey, white and black. My logo is orange in colour.

Target Market(s)

Age 18 to 35

Industry/Entity Type

Online

Font styles to use
Sans Serif
Decorative

Colors
f78f20
919191
eaeaea
000000

Requirements
Must have
• Must have good flow of information and represented with graphic.
Nice to have
• My project is nice to be simple to understand.
Should not have
• My project must not have alot of words.

```html
<!DOCTYPE html>
<html lang="en">
<head>
<meta charset="utf-8">
<title>Lumaro Specs – How to Choose Your Lenses</title>
<link href="https://fonts.googleapis.com/css2?family=Open+Sans:wght@400;600;700;800&family=Oswald:wght@500;700&display=swap" rel="stylesheet">
<style>
  :root {
    --orange: #f78f20;
    --orange-deep: #e07a10;
    --grey: #919191;
    --light: #eaeaea;
    --black: #000000;
    --ink: #141414;
    --panel: #262626;
    --white: #ffffff;
  }
  * { box-sizing: border-box; margin: 0; padding: 0; }
  html, body { width: 841px; height: 1200px; overflow: hidden; background: var(--ink); }
  .infographic {
    position: relative; width: 841px; height: 1200px; overflow: hidden;
    background: radial-gradient(ellipse at 50% 40%, #262626 0%, #141414 70%);
    font-family: "Open Sans", Arial, sans-serif; color: var(--white);
  }
  .title-banner {
    position: absolute; left: 28px; top: 14px; width: 785px; height: 50px;
    background: var(--orange); color: var(--ink);
    font-weight: 800; font-size: 30px; text-align: center; line-height: 50px;
  }
  .tagline {
    position: absolute; left: 28px; top: 64px; width: 785px; height: 30px;
    background: var(--black); font-size: 16px; text-align: center; line-height: 30px;
  }
  .steps-bar {
    position: absolute; left: 28px; top: 100px; width: 785px; height: 36px;
    background: var(--orange); color: var(--ink);
    font-weight: 700; font-size: 22px; text-align: center; line-height: 36px;
  }
  .step-head { position: absolute; top: 156px; display: flex; align-items: center; gap: 16px; }
  .step-head.left { left: 28px; }
  .step-head.right { right: 28px; flex-direction: row-reverse; text-align: right; }
  .step-badge {
    width: 70px; height: 70px; border-radius: 50%; background: var(--grey);
    border: 4px solid var(--light); color: var(--white);
    font-family: "Oswald", Arial, sans-serif; font-size: 40px; font-weight: 700;
    display: flex; align-items: center; justify-content: center;
  }
  .step-label { font-size: 20px; line-height: 1.25; }
  .glasses-icon {
    position: absolute; left: 325px; top: 168px; width: 190px; height: 58px;
    background: linear-gradient(90deg, #e6e6e6, #bdbdbd); border-radius: 10px;
  }
  .divider {
    position: absolute; left: 419px; top: 270px; height: 630px;
    border-left: 3px dashed var(--grey);
  }
  .card { position: absolute; display: flex; height: var(--h); }
  .card-text {
    background: var(--orange); flex: 1; padding: 0 16px;
    display: flex; align-items: center; justify-content: center; text-align: center;
    font-size: 18px; line-height: 1.35; font-weight: 600;
  }
  .card-text strong { font-weight: 800; color: var(--ink); }
  .card-num {
    width: 100px; background: var(--orange-deep);
    display: flex; align-items: center; justify-content: center;
    font-family: "Oswald", Arial, sans-serif; font-size: 62px; font-weight: 700;
  }
  .calc .card-num { clip-path: polygon(0 0, 78% 0, 100% 50%, 78% 100%, 0 100%); padding-right: 18px; }
  .calc { left: 28px; width: 378px; }
  .match { left: 435px; width: 378px; }
  .match .card-num { clip-path: polygon(0 50%, 22% 0, 100% 0, 100% 100%, 22% 100%); padding-left: 18px; }
  .note {
    position: absolute; left: 450px; top: 716px; width: 350px;
    text-align: center; font-size: 18px; line-height: 1.35;
  }
  .attributes-head {
    position: absolute; left: 28px; top: 946px; width: 300px; height: 40px;
    background: var(--orange); color: var(--ink);
    font-weight: 700; font-size: 22px; line-height: 40px; padding-left: 18px;
    clip-path: polygon(0 0, 92% 0, 100% 50%, 92% 100%, 0 100%);
  }
  .attribute-list { position: absolute; left: 28px; top: 1000px; width: 430px; list-style: none; }
  .attribute-list li {
    display: flex; align-items: center; height: 32px; margin-bottom: 6px;
    background: var(--panel); font-size: 17px;
  }
  .attribute-list .idx {
    width: 32px; height: 32px; background: var(--grey); margin-right: 12px;
    display: flex; align-items: center; justify-content: center;
    font-weight: 700; color: var(--white);
  }
  .brand {
    position: absolute; left: 540px; top: 1050px; display: flex; align-items: center; gap: 12px;
    color: var(--grey); font-weight: 800; font-size: 34px;
  }
  .brand-dot { width: 22px; height: 22px; border-radius: 50%; background: var(--grey); }
</style>
</head>
<body>
<main class="infographic">
  <h1 class="title-banner">Thin: Super Thin or Ultra Thin Lens?</h1>
  <p class="tagline">Thinner lenses always make your spectacles look and fit better</p>
  <h2 class="steps-bar">Choose your lenses in 2 easy steps!</h2>

  <div class="step-head left"><span class="step-badge">1</span><span class="step-label">Calculate your<br>power</span></div>
  <div class="glasses-icon" role="img" aria-label="White outline icon of a pair of glasses"></div>
  <div class="step-head right"><span class="step-badge">2</span><span class="step-label">Match your power<br>with your lens</span></div>

  <div class="divider"></div>

  <div class="card calc" style="top:275px;--h:117px"><div class="card-text"><span>Your prescription may look like this:<br><strong>-2.50 / -1.50 x 150</strong></span></div><div class="card-num">1</div></div>
  <div class="card calc" style="top:415px;--h:131px"><div class="card-text"><span>Take the first power which is <strong>2.50</strong>, and add half of the second power <strong>1.50</strong>.</span></div><div class="card-num">2</div></div>
  <div class="card calc" style="top:574px;--h:76px"><div class="card-text"><span>The concluding power is <strong>3.25</strong>!</span></div><div class="card-num">3</div></div>
  <div class="card calc" style="top:672px;--h:84px"><div class="card-text"><span>Do the same for the other eye</span></div><div class="card-num">4</div></div>
  <div class="card calc" style="top:778px;--h:112px"><div class="card-text"><span>If the signs are different, subtract the numbers from each other.</span></div><div class="card-num">5</div></div>

  <div class="card match" style="top:275px;--h:117px"><div class="card-num">1</div><div class="card-text"><span>Thin lenses are fitted by default. They are suitable for power below <strong>4.00</strong>.</span></div></div>
  <div class="card match" style="top:415px;--h:131px"><div class="card-num">2</div><div class="card-text"><span>Thinner 1.67 index lenses are recommended if your power is between <strong>4.00 and 7.00</strong></span></div></div>
  <div class="card match" style="top:574px;--h:112px"><div class="card-num">3</div><div class="card-text"><span>Thinnest 1.74 index lenses are recommended if your power is above <strong>7.00</strong>.</span></div></div>

  <p class="note">You may choose lenses thinner or thicker than recommended but keep in mind thinner lenses always make your spectacles look and fit better!</p>

  <h2 class="attributes-head">Attributes of our Lenses</h2>
  <ul class="attribute-list">
    <li><span class="idx">1</span>Aspheric design – for sharper vision</li>
    <li><span class="idx">2</span>UV and blue light protection</li>
    <li><span class="idx">3</span>Multicoated Scratch Resistance</li>
    <li><span class="idx">4</span>Lightweight technology</li>
  </ul>

  <div class="brand"><span class="brand-dot"></span>Lumaro Specs</div>
</main>
</body>
</html>
```